Court Heritage Trust Business Card

We need a business card design for the Court Heritage Trust. It is a non-profit organization that promotes environmental awareness and activism within the tennis community. It will include our newly designed logo. It needs to be modern yet with an elegant business feel. The market we deal with is upscale with discerning taste. Must convey a sense of seriousness that people can trust, while inspiring their highest values to create a better world.
Target Market(s)
Upscale market of tennis, business, and environmental enthusiasts
Industry/Entity Type
Non-Profit
Requirements
Must have
- Must have an elegant look, be easy to read and convey seriousness of purpose.
Show where you will place the name, title, address, email and phone number on front of the card.
Note: We have included both versions of our new logo. Feel free to use either or both. We are not sure which will be ideal for a business card. The files are in jpg. We can supply other formats if they will be easier to work with.
Nice to have
- The back side should have the following:
Printed by "PLIX" on:
100% recycled post consumer waste
100% recyclable and biodegradable
Sustainable source, Elemental Chlorine Free (ECF)
Manufactured using wind power
Include the plix logo from the images section.

```html
<!DOCTYPE html>
<html lang="en">
<head>
<meta charset="utf-8">
<title>Court Heritage Trust – Business Card</title>
<link href="https://fonts.googleapis.com/css2?family=Open+Sans:wght@300;400;600;700&display=swap" rel="stylesheet">
<style>
  :root{
    --teal:#2a93b6;
    --teal-deep:#16708f;
    --teal-light:#2ea3c6;
    --ink:#4a4f55;
    --grey-icon:#8e969c;
    --paper:#ffffff;
    --bg:#e9eaec;
    --leaf:#8cc63f;
    --eco-text:#9fd46a;
  }
  *{margin:0;padding:0;box-sizing:border-box}
  html,body{width:1200px;height:1023px;overflow:hidden}
  body{background:var(--bg);font-family:"Open Sans",Arial,sans-serif;position:relative}
  .card{position:absolute;left:220px;width:760px;height:434px;border-radius:4px;box-shadow:0 6px 20px rgba(0,0,0,.18);overflow:hidden}
  .card-front{top:60px;background:var(--paper)}
  .card-back{top:529px;background:radial-gradient(ellipse at 60% 40%,var(--teal-light) 0%,var(--teal) 45%,var(--teal-deep) 100%)}

  .org-title{position:absolute;left:54px;top:66px;font-weight:300;font-size:40px;letter-spacing:1px;color:var(--teal);text-transform:uppercase;white-space:nowrap}
  .brand-mark{position:absolute;right:56px;top:44px;width:220px;display:flex;flex-direction:column;align-items:center;gap:16px;font-weight:600;font-size:17px;color:var(--teal);text-align:center}
  .brand-mark .dot{width:140px;height:140px;border-radius:50%;background:var(--teal)}

  .person{position:absolute;left:56px;top:150px}
  .person-name{font-weight:700;font-size:22px;color:var(--teal);text-transform:uppercase;letter-spacing:.5px}
  .person-role{font-size:15px;color:var(--ink);margin-top:2px}

  .contacts{position:absolute;left:56px;top:222px;list-style:none}
  .contacts li{display:flex;align-items:center;gap:10px;font-size:16px;color:var(--ink);height:27px}
  .contacts svg{width:18px;height:18px;flex:none}

  .org-footer{position:absolute;left:56px;top:340px}
  .org-footer .org-name{font-weight:700;font-size:16px;color:var(--teal)}
  .org-footer .address{font-size:16px;color:var(--ink);margin-top:8px}

  .back-brand{position:absolute;left:0;right:0;top:130px;display:flex;flex-direction:column;align-items:center;gap:18px}
  .back-brand .dot{width:40px;height:40px;border-radius:50%;border:3px solid #fff}
  .back-brand .name{color:#fff;font-size:30px;font-weight:400;letter-spacing:1px;text-transform:uppercase}

  .eco{position:absolute;left:34px;bottom:30px;display:flex;gap:16px;align-items:flex-start}
  .eco-badge{width:42px;height:42px;border-radius:50%;background:var(--leaf);color:#fff;font-size:12px;font-weight:600;display:flex;align-items:center;justify-content:center;flex:none}
  .eco-text{color:var(--eco-text);font-size:14px;line-height:21px}
</style>
</head>
<body>
  <section class="card card-front" aria-label="Business card front">
    <h1 class="org-title">Court Heritage Trust</h1>
    <div class="brand-mark"><span class="dot"></span>Court Heritage Trust</div>

    <div class="person">
      <div class="person-name">Daniel Hart</div>
      <div class="person-role">Director</div>
    </div>

    <ul class="contacts">
      <li>
        <svg viewBox="0 0 18 18"><circle cx="9" cy="9" r="9" fill="var(--grey-icon)"/><rect x="5" y="5" width="8" height="8" rx="1" fill="#fff"/><rect x="6.5" y="7" width="5" height="2" fill="var(--grey-icon)"/></svg>
        0140 555 0182
      </li>
      <li>
        <svg viewBox="0 0 18 18"><circle cx="9" cy="9" r="9" fill="var(--grey-icon)"/><path d="M6 5c-1 1-1 3 1 5.5S11 14 12.5 13l.7-1.3-2-1.3-1 .8c-1-.5-2-1.7-2.4-2.6l.8-.9-1.2-2.1z" fill="#fff"/></svg>
        0160 555 0147
      </li>
      <li>
        <svg viewBox="0 0 18 18"><circle cx="9" cy="9" r="9" fill="var(--grey-icon)"/><rect x="4.5" y="6" width="9" height="6.5" rx="1" fill="#fff"/><path d="M4.8 6.5 9 9.8l4.2-3.3" stroke="var(--grey-icon)" stroke-width="1" fill="none"/></svg>
        danielhart@postmail.net
      </li>
      <li>
        <svg viewBox="0 0 18 18"><circle cx="9" cy="9" r="9" fill="var(--grey-icon)"/><circle cx="9" cy="9" r="5" fill="none" stroke="#fff" stroke-width="1.2"/><path d="M4 9h10M9 4c-2.5 3-2.5 7 0 10M9 4c2.5 3 2.5 7 0 10" stroke="#fff" stroke-width="1" fill="none"/></svg>
        www.courtheritagetrust.org
      </li>
    </ul>

    <div class="org-footer">
      <div class="org-name">Court Heritage Trust</div>
      <div class="address">P.O Box 214 Linden Street, Fairview, Westbrook</div>
    </div>
  </section>

  <section class="card card-back" aria-label="Business card back">
    <div class="back-brand">
      <span class="dot"></span>
      <div class="name">Court Heritage Trust</div>
    </div>

    <div class="eco">
      <div class="eco-badge">plix</div>
      <p class="eco-text">
        Printed by "PLIX" on:<br>
        100% recycled post consumer waste - 100% recyclable and biodegradable<br>
        Sustainable source, Elemental Chlorine Free (ECF) - Manufactured using wind power
      </p>
    </div>
  </section>
</body>
</html>
```